Kavenzira Wines

A Red Wine Label for future Wine Concept called Kavenzira Wine. The back label will have the following words which capture the essence of the wine "I am sworn to the secrecy about the origins of this wine but I can assure you it’s from the best cellars of Africa. Kavenzira is an African (Shona) name which loosely means honour, praise or to be held in high exteem. Hold on to your hats because this wine is a whirlwind of flavours. It's dark, spicy and fruity flavours will attack the palate with warm aggression and intent whilst being served with Sadza/ Nsima and roasted beef accompanied with mufushwa (dried vegetables) cooked in grounded nut paste. The inspiring flame, style and mood of an African braai, together with its outlandish flavours popping in and out of the glass, Kavenzira will make every serving a gesture of respect and distinction!!!"
Updates

I will be buying wine packed in unbranded bottles then Brand it as Kavenzira on my own Kavenzira label for some African event theme. The wines will be South African a Shiraz. So I need a back label with message placed in brief and front label for a red wine bottle. I have attached some old labels for the wine so I need a redesign of the l label for have a morden and African feel to it                                   

Please

Target Market(s)

Appeal to general populace and those with an afrocentric feel

Requirements
Must have
• Back and front labels, simplicity
Should not have
• Too many colours

```html
<!DOCTYPE html>
<html lang="en">
<head>
<meta charset="utf-8">
<title>Kavenzira Wine – Shiraz Front Label</title>
<link rel="stylesheet" href="https://fonts.googleapis.com/css2?family=Lato:wght@300;400&display=swap">
<style>
  :root {
    --backdrop: #f4efe4;
    --label-red: #b0331f;
    --label-red-deep: #a32d1a;
    --artwork-tone: #bb4222;
    --gold: #f2a634;
    --gold-soft: #e89a2e;
  }
  html, body {
    margin: 0;
    padding: 0;
    width: 960px;
    height: 1200px;
    overflow: hidden;
    background: var(--backdrop);
  }
  .canvas {
    position: relative;
    width: 960px;
    height: 1200px;
    background: var(--backdrop);
    font-family: "Lato", sans-serif;
  }
  .front-label {
    position: absolute;
    left: 270px;
    top: 65px;
    width: 420px;
    height: 1070px;
    background: var(--label-red);
    box-sizing: border-box;
    color: var(--gold);
  }
  .front-label__frame-outer {
    position: absolute;
    inset: 10px;
    border: 1.5px solid var(--gold-soft);
  }
  .front-label__frame-inner {
    position: absolute;
    inset: 17px;
    border: 1px solid var(--gold-soft);
  }
  .brand-name {
    position: absolute;
    top: 78px;
    left: 0;
    right: 0;
    margin: 0;
    text-align: center;
    font-weight: 300;
    font-size: 50px;
    letter-spacing: 3px;
    color: var(--gold);
  }
  .sun-artwork {
    position: absolute;
    top: 240px;
    left: 34px;
    width: 352px;
    height: 370px;
    background: linear-gradient(180deg, var(--artwork-tone), var(--label-red-deep));
  }
  .varietal {
    position: absolute;
    top: 708px;
    left: 0;
    right: 0;
    margin: 0;
    text-align: center;
    font-weight: 300;
    font-size: 62px;
    letter-spacing: 2px;
    color: var(--gold);
  }
  .varietal-divider {
    position: absolute;
    top: 792px;
    left: 203px;
    width: 14px;
    height: 2px;
    background: var(--gold);
  }
  .origin {
    position: absolute;
    top: 814px;
    left: 0;
    right: 0;
    margin: 0;
    text-align: center;
    font-weight: 300;
    font-size: 35px;
    letter-spacing: 1px;
    color: var(--gold);
  }
  .bottle-facts {
    position: absolute;
    left: 30px;
    right: 30px;
    top: 1004px;
    display: flex;
    justify-content: space-between;
    font-weight: 400;
    font-size: 24px;
    color: var(--gold);
  }
</style>
</head>
<body>
  <main class="canvas">
    <section class="front-label">
      <div class="front-label__frame-outer"></div>
      <div class="front-label__frame-inner"></div>
      <h1 class="brand-name">Kavenzira</h1>
      <div class="sun-artwork" role="img" aria-label="Brush-stroke sun illustration with birds in flight above a horizon line"></div>
      <h2 class="varietal">SHIRAZ</h2>
      <div class="varietal-divider"></div>
      <p class="origin">SOUTH AFRICA</p>
      <div class="bottle-facts">
        <span class="bottle-facts__abv">12% Vol.</span>
        <span class="bottle-facts__volume">700ml</span>
      </div>
    </section>
  </main>
</body>
</html>
```